Flyer-Design für Marktplatz der bäuerlichen Landwirtschaft
Zielgruppe
Der stilleHalmkrone stellt einen Marktplatz der bäuerlichen Landwirtschaft zur Verfügung.
Zielgruppe 1: Lieferanten, bäuerliche Direktvermarkter mit herausragenden Produkten die für eine weitere Vertriebsmöglichkeit für Ihre Produkte offen sind.
Zielgruppe 2: Kunden, die auf der Suche nach mit Liebe hergestellten Produkten aus der bäuerlichen Landwirtschaft sind. Sie sind bereit für ein gutes Produkt auch einen entsprechenden Preis zu zahlen.
Aufgabenstellung
Es soll ein Flyer im Postkartenformat DIN A6 – quer designt werden.
Das Ergebnis soll sowohl, als Datei direkt der Druckerei übergeben werden und auch im eps-Format bereitgestellt werden. Auf Hinweis eines Designers das es ggf. schwer wird die Datei im EPS bereitzustellen könnten wir darauf auch verzichten.
Wir haben unser Logo und die Schriftart als Dateien zur Verfügung gestellt.
Der Eindruck soll sehr hochwertig sein und dabei Bodenständigkeit ausdrücken. Das Design soll sehr elegant sein, wobei ein wenig Verspieltheit in Ordnung ist. Bitte darauf achten, dass an den Seitenrändern einen Sicherheitsabstand von 4mm für Schrift oder Logo eingehalten werden muss.
Auf Seite 1 sollen folgende Objekte platziert werden:
• Logo – (Hier kann die Anordnung der Schriftzüge „stiller“ und „Halmkrone“ gerne noch optimiert werden.)
• Slogan: „Marktplatz der bäuerlichen Landwirtschaft“
• Internetadresse: www.stillerHalmkrone.de
Als Hintergrundfarbe wünschen wir uns eine pastellige lindgrüne Hintergrundfarbe.
Auf Seite 2 sollen folgende Objekte platziert werden:
• Ein Block / Bereich, der ca. 1/3 der Seite ausmacht, der abgesetzt ist um eine persönliche Ansprache zu ermöglichen (Entweder Stempel oder handschriftliche Ansprache). Dieser Block sollte mit „Für Dich“ überschrieben sein (Gerne auch eine andere gute offene Überschrift für den Block nutzen)
• Hier können wir uns eine Mischung aus pastelligem Grau und Blau vorstellen (Gerne auch eine eigene pastellige Ideen einbringen)
• Jetzt fehlt uns nur noch ein Satz, der die Betrachter zum Besuch der Webseite einladen soll. Der im übrigen Teil dargestellt werden soll.
• Je nach Design kann evtl. das Logo in einer kleineren Darstellung mit integriert werden.
Für Rückfragen stehen wir gerne zur Verfügung.
Wir freuen uns auf Eure Entwürfe

```html
<!DOCTYPE html>
<html lang="de">
<head>
<meta charset="utf-8">
<title>stiller Halmkrone – Postkarte</title>
<link rel="stylesheet" href="https://fonts.googleapis.com/css2?family=Marcellus&family=Ubuntu:wght@500;700&display=swap">
<style>
  :root {
    --page-bg: #e6e6e6;
    --lime-deep: #4f9a2e;
    --lime-mid: #7cb84a;
    --lime-light: #a9d27a;
    --wood-dark: #3f7a2a;
    --field-gold: #e2b21c;
    --sky-light: #eaf6fb;
    --sky-blue: #5cc4ec;
    --field-blue: #2e9fd0;
    --ink-white: #ffffff;
    --brand-brown: #8a5a3c;
    --bubble-green: #4a9a2a;
  }
  * { margin: 0; padding: 0; box-sizing: border-box; }
  html, body { width: 1200px; height: 676px; overflow: hidden; }
  body { background: var(--page-bg); position: relative; }

  .card {
    position: absolute;
    top: 138px;
    width: 562px;
    height: 399px;
    overflow: hidden;
  }
  .card--front { left: 29px; }
  .card--back { left: 609px; }
  .card svg.card__art { position: absolute; inset: 0; width: 100%; height: 100%; }

  .brand {
    position: absolute;
    left: 22px;
    top: 150px;
    top: 62px;
    display: flex;
    align-items: center;
    gap: 6px;
    font-family: "Marcellus", serif;
    font-size: 15px;
    color: var(--brand-brown);
  }
  .brand__dot {
    width: 9px; height: 9px; border-radius: 50%;
    background: var(--brand-brown);
  }

  .front__slogan {
    position: absolute;
    left: 0; right: 0;
    top: 336px;
    text-align: center;
    font-family: "Marcellus", serif;
    font-size: 25px;
    color: var(--ink-white);
  }
  .front__url {
    position: absolute;
    left: 0; right: 0;
    top: 367px;
    text-align: center;
    font-family: "Ubuntu", sans-serif;
    font-weight: 700;
    font-size: 15px;
    color: var(--ink-white);
  }

  .note-box {
    position: absolute;
    left: 21px; top: 102px;
    width: 260px; height: 212px;
    background: var(--ink-white);
    box-shadow: 0 0 4px rgba(0,0,0,0.15);
  }
  .greeting {
    position: absolute;
    left: 54px; top: 32px;
    width: 126px; height: 52px;
    border-radius: 50%;
    background: var(--ink-white);
    box-shadow: 0 1px 3px rgba(0,0,0,0.25);
    display: flex; align-items: center; justify-content: center;
    font-family: "Ubuntu", sans-serif;
    font-weight: 700;
    font-size: 22px;
    color: var(--bubble-green);
  }
  .farmer-figure {
    position: absolute;
    left: 28px; top: 62px;
    width: 12px; height: 40px;
    background: linear-gradient(#6b4a36, #2c2c2c);
    border-radius: 3px;
  }
  .invite {
    position: absolute;
    left: 282px; top: 318px;
    width: 270px;
    transform: rotate(-9deg);
    transform-origin: left top;
    font-family: "Ubuntu", sans-serif;
    font-weight: 700;
    color: var(--ink-white);
    text-align: right;
    line-height: 1.15;
    text-shadow: 0 1px 2px rgba(0,60,100,0.4);
  }
  .invite__line { font-size: 16px; }
  .invite__url { font-size: 13px; }
</style>
</head>
<body>

<section class="card card--front">
  <svg class="card__art" viewBox="0 0 562 399" aria-hidden="false">
    <defs>
      <linearGradient id="woodFill" x1="0" y1="0" x2="1" y2="1">
        <stop offset="0" stop-color="#d9ecb5"/>
        <stop offset="0.25" stop-color="#6fa84a"/>
        <stop offset="1" stop-color="var(--wood-dark)"/>
      </linearGradient>
      <linearGradient id="fieldFill" x1="0" y1="0" x2="0" y2="1">
        <stop offset="0" stop-color="#f4f8fb"/>
        <stop offset="0.5" stop-color="#cfe0a8"/>
        <stop offset="0.75" stop-color="var(--field-gold)"/>
        <stop offset="1" stop-color="#c99a1a"/>
      </linearGradient>
      <linearGradient id="bandFill" x1="0" y1="0" x2="0" y2="1">
        <stop offset="0" stop-color="var(--lime-mid)"/>
        <stop offset="1" stop-color="var(--lime-deep)"/>
      </linearGradient>
    </defs>
    <rect class="front__backdrop" width="562" height="399" fill="url(#woodFill)" role="img" aria-label="Grüner Holzzaun mit eingeritztem Herz, Sonnenlicht oben links"/>
    <path class="front__window" role="img" aria-label="Herzförmiger Ausblick auf einen Traktor bei der Feldarbeit im goldenen Abendlicht"
      d="M325,124 C300,60 250,40 210,45 C160,50 145,100 158,140 C175,200 250,250 295,309 C360,240 440,190 470,140 C500,90 480,45 430,43 C380,42 345,70 325,124 Z"
      fill="url(#fieldFill)" stroke="#2f5f1f" stroke-width="2"/>
    <path class="front__band" d="M0,337 C180,320 420,300 562,237 L562,399 L0,399 Z" fill="url(#bandFill)"/>
    <path class="front__band-edge" d="M0,337 C180,320 420,300 562,237" fill="none" stroke="#c7e4a2" stroke-width="2" opacity="0.7"/>
  </svg>

  <div class="brand">
    <span class="brand__dot"></span>
    <span class="brand__name">stiller Halmkrone</span>
  </div>

  <p class="front__slogan">Marktplatz der bäuerlichen Landwirtschaft</p>
  <p class="front__url">www.stillerHalmkrone.de</p>
</section>

<section class="card card--back">
  <svg class="card__art" viewBox="0 0 562 399">
    <defs>
      <linearGradient id="skyFill" x1="0" y1="0" x2="0.6" y2="1">
        <stop offset="0" stop-color="var(--sky-light)"/>
        <stop offset="0.45" stop-color="var(--sky-blue)"/>
        <stop offset="1" stop-color="var(--field-blue)"/>
      </linearGradient>
    </defs>
    <rect width="562" height="399" fill="url(#skyFill)" role="img" aria-label="Blau getöntes Foto eines Traktors mit Heuwender auf einer Wiese unter hellem Himmel"/>
  </svg>

  <div class="farmer-figure" role="img" aria-label="Kleine gezeichnete Bauernfigur mit Heugabel"></div>
  <div class="greeting">Für Dich!</div>
  <div class="note-box" aria-label="Freier Bereich für persönliche Ansprache"></div>

  <div class="invite">
    <p class="invite__line">Wir freuen uns auf Dich unter:</p>
    <p class="invite__url">www.stillerHalmkrone.de</p>
  </div>
</section>

</body>
</html>
```